Business Cards for our company

Hi there,

we have successfully designed a logo with ArtFlock and would like now to design our business cards. We would like to keep the colours and the look-and-feel of the logo. Please send in variations with two or three colours and one or two sides. I promise to respond to every single submission.

Many thanks and happy new year.

All the best,
Wilfried

Target Market(s)

B2B

Industry/Entity Type

Trade

Contact Information for Business Card

We have successfully designed a logo with ArtFlock and would like now to design our business cards. We would like to keep the colours and the look-and-feel of the logo. Please send in variations with two or three colours and one or two sides. I promise to respond to every single submission.

Font styles to use
Serif
Sans Serif
Script

Requirements
Must have
• These information should be on the business card, grouped as you suggest, and we think using small pictograms for mobile, email, etc is pretty helpful:
• Wilfried Tammler (first and second name)
• Geschäftsführer/ Managing Director (title)
• KoR Warenkontor GmbH (company name and legal form)
• Ostheimer Str. 18/3 (street and house number)
• 70839 Gerlingen (zip code and town)
• +491709384562 (mobile)
• +4971569027341 (work)
• w.tammler@kor-warenkontor.example (email)
• www.kor-warenkontor.example (web)
Nice to have
• Spectacular and interesting layout and design. You look at it and think, wow, that's not the normal stuff.
• We think of ourselves as bridge-builders between businesses (international producers on the one hand, and retail chains on the other hand) and we translate, organise and manage projects where both partners are involved, but it's difficult for them to cooperate due to language barriers and different working cultures.
• This is why we have the n between the B's shaped as a bridge, and the green arc supports this idea. Maybe you could play with this idea...
Should not have
• the standard layout that everybody has

```html
<!DOCTYPE html>
<html lang="en">
<head>
<meta charset="utf-8">
<title>KoR Warenkontor – Business Cards</title>
<link rel="stylesheet" href="https://fonts.googleapis.com/css2?family=Open+Sans:wght@400;600;700&family=Arimo:wght@400&display=swap">
<style>
  :root {
    --backdrop: #e9e7e4;
    --card: #1c1c1c;
    --card-edge: #262626;
    --white: #ffffff;
    --green: #2fa84a;
    --soft: #e6e6e6;
  }
  * { box-sizing: border-box; margin: 0; padding: 0; }
  html, body {
    width: 1200px; height: 1200px; overflow: hidden;
    background: var(--backdrop);
  }
  .sheet {
    width: 1200px; height: 1200px;
    display: flex; flex-direction: column;
    align-items: center; justify-content: center; gap: 60px;
  }
  .card {
    position: relative;
    width: 860px; height: 491px;
    border-radius: 26px;
    background: radial-gradient(ellipse at 40% 30%, var(--card-edge), var(--card) 70%);
    box-shadow: 0 10px 30px rgba(0,0,0,0.25);
    overflow: hidden;
  }
  .wordmark {
    position: absolute;
    display: flex; align-items: center; gap: 14px;
    font-family: "Open Sans", sans-serif;
    font-weight: 700;
    color: var(--white);
    white-space: nowrap;
    line-height: 1;
  }
  .wordmark-dot {
    width: 18px; height: 18px; border-radius: 50%;
    background: var(--green);
    flex: none;
  }
  .card-front .wordmark {
    left: 50%; top: 50%; transform: translate(-50%, -50%);
    font-size: 52px;
  }
  .card-back .wordmark {
    right: 60px; top: 90px;
    font-size: 44px;
  }
  .person {
    position: absolute; right: 470px; top: 252px;
    text-align: right; font-family: "Open Sans", sans-serif;
    white-space: nowrap;
  }
  .person-name { color: var(--white); font-size: 26px; font-weight: 600; }
  .person-role { color: var(--green); font-size: 17px; font-weight: 400; margin-top: 2px; }
  .divider {
    position: absolute; left: 418px; top: 252px;
    width: 3px; height: 168px; background: var(--green);
  }
  .contacts {
    position: absolute; left: 440px; top: 252px;
    list-style: none;
    font-family: "Arimo", sans-serif; font-size: 18px; color: var(--soft);
    white-space: nowrap;
  }
  .contacts li {
    display: flex; align-items: center; gap: 12px;
    height: 28px;
  }
  .contacts svg { width: 18px; height: 18px; flex: none; }
</style>
</head>
<body>
<main class="sheet">
  <section class="card card-front" aria-label="Card front">
    <div class="wordmark"><span class="wordmark-dot"></span><span>KoR Warenkontor GmbH</span></div>
  </section>

  <section class="card card-back" aria-label="Card back">
    <div class="wordmark"><span class="wordmark-dot"></span><span>KoR Warenkontor GmbH</span></div>

    <div class="person">
      <p class="person-name">Wilfried Tammler</p>
      <p class="person-role">Managing Director</p>
    </div>

    <div class="divider"></div>

    <ul class="contacts">
      <li>
        <svg viewBox="0 0 20 20" aria-hidden="true"><rect width="20" height="20" rx="2" fill="#2fa84a"/><rect x="7" y="4" width="6" height="12" rx="1" fill="none" stroke="#fff" stroke-width="1.5"/></svg>
        <span>+491709384562</span>
      </li>
      <li>
        <svg viewBox="0 0 20 20" aria-hidden="true"><rect width="20" height="20" rx="2" fill="#2fa84a"/><path d="M6 5c-1 1-1 3 1 6s4 4 6 4l1-2-2-1-1 1c-1 0-3-2-3-3l1-1-1-2z" fill="#fff"/></svg>
        <span>+4971569027341</span>
      </li>
      <li>
        <svg viewBox="0 0 20 20" aria-hidden="true"><rect width="20" height="20" rx="2" fill="#2fa84a"/><path d="M10 4a4 4 0 0 0-4 4c0 3 4 8 4 8s4-5 4-8a4 4 0 0 0-4-4z" fill="#fff"/><circle cx="10" cy="8" r="1.5" fill="#2fa84a"/></svg>
        <span>Ostheimer Str. 18/3</span>
      </li>
      <li>
        <svg viewBox="0 0 20 20" aria-hidden="true"><rect width="20" height="20" rx="2" fill="none"/></svg>
        <span>70839 Gerlingen</span>
      </li>
      <li>
        <svg viewBox="0 0 20 20" aria-hidden="true"><rect width="20" height="20" rx="2" fill="#2fa84a"/><circle cx="10" cy="10" r="5.5" fill="none" stroke="#fff" stroke-width="1.3"/><path d="M4.5 10h11M10 4.5c-3 3-3 8 0 11M10 4.5c3 3 3 8 0 11" fill="none" stroke="#fff" stroke-width="1"/></svg>
        <span>www.kor-warenkontor.example</span>
      </li>
      <li>
        <svg viewBox="0 0 20 20" aria-hidden="true"><rect width="20" height="20" rx="2" fill="#2fa84a"/><rect x="4" y="6" width="12" height="8" fill="none" stroke="#fff" stroke-width="1.3"/><path d="M4 6l6 5 6-5" fill="none" stroke="#fff" stroke-width="1.3"/></svg>
        <span>w.tammler@kor-warenkontor.example</span>
      </li>
    </ul>
  </section>
</main>
</body>
</html>
```